Notepads for Marketing pieces-BOLD design

Looking for notepads for marketing pieces with logo, phone number, and website. Maybe something faded in background. Looking for bold and different

```html
<!DOCTYPE html>
<html lang="en">
<head>
<meta charset="utf-8">
<title>Vitalis Care Notepad</title>
<link href="https://fonts.googleapis.com/css2?family=Jost:wght@600;800&family=Roboto:wght@400&display=swap" rel="stylesheet">
<style>
  :root {
    --backdrop: #8c8c8c;
    --paper: #ffffff;
    --brand-red: #d0121b;
    --ink: #111111;
    --rule: #6e6e6e;
    --photo-light: #f2f2f2;
    --photo-mid: #c9c9c9;
    --photo-dark: #8f8f8f;
    --footer-text: #ffffff;
  }
  * { margin: 0; padding: 0; box-sizing: border-box; }
  html, body { width: 1200px; height: 802px; overflow: hidden; }
  body { background: var(--backdrop); position: relative; }

  .notepad-sheet {
    position: absolute;
    left: 338px; top: 31px;
    width: 524px; height: 740px;
    background: var(--paper);
    box-shadow: 0 14px 22px rgba(0,0,0,0.3);
    overflow: hidden;
  }

  .background-photo {
    position: absolute;
    left: 0; top: 349px;
    width: 100%; height: 318px;
    background:
      linear-gradient(to bottom, rgba(255,255,255,0.85) 0%, rgba(255,255,255,0) 45%),
      linear-gradient(120deg, var(--photo-light) 0%, var(--photo-mid) 40%, var(--photo-dark) 75%, var(--photo-mid) 100%);
  }

  .brand-name {
    position: absolute;
    top: 74px; left: 0; width: 100%;
    text-align: center;
    font-family: "Jost", sans-serif;
    font-weight: 800;
    font-size: 44px;
    letter-spacing: 2px;
    color: var(--brand-red);
    text-transform: uppercase;
    line-height: 1;
  }

  .service-line {
    position: absolute;
    top: 140px; left: 0; width: 100%;
    text-align: center;
    font-family: "Jost", sans-serif;
    font-weight: 600;
    font-size: 11px;
    color: var(--ink);
  }

  .writing-lines {
    position: absolute;
    left: 89px; top: 236px;
    width: 362px; height: 378px;
    background: repeating-linear-gradient(to bottom, var(--rule) 0, var(--rule) 1px, transparent 1px, transparent 16.4px);
  }

  .contact-footer {
    position: absolute;
    left: 0; bottom: 0;
    width: 100%; height: 73px;
    background: var(--brand-red);
    color: var(--footer-text);
    font-family: "Roboto", sans-serif;
    font-size: 9.5px;
  }
  .contact-item {
    position: absolute;
    top: 0; height: 73px;
    display: flex; align-items: center; gap: 8px;
  }
  .contact-item svg { flex: none; }
  .contact-email { left: 58px; }
  .contact-phone { left: 212px; }
  .contact-address { left: 357px; line-height: 1.35; }
  .footer-divider {
    position: absolute;
    top: 12px; width: 1px; height: 39px;
    background: var(--footer-text);
  }
  .divider-one { left: 181px; }
  .divider-two { left: 342px; }
</style>
</head>
<body>
  <div class="notepad-sheet">
    <div class="background-photo" role="img" aria-label="Faded black and white photo of a caregiver taking a patient's blood pressure"></div>

    <div class="brand-name">Vitalis Care</div>
    <div class="service-line">Home Health | Medical Staffing | Outpatient Therapy</div>

    <div class="writing-lines"></div>

    <div class="contact-footer">
      <div class="contact-item contact-email">
        <svg width="16" height="12" viewBox="0 0 16 12"><rect x="0.75" y="0.75" width="14.5" height="10.5" fill="none" stroke="#fff" stroke-width="1.3"/><polyline points="1,1 8,7 15,1" fill="none" stroke="#fff" stroke-width="1.3"/></svg>
        <span>vitaliscare.org</span>
      </div>
      <div class="footer-divider divider-one"></div>
      <div class="contact-item contact-phone">
        <svg width="14" height="14" viewBox="0 0 24 24"><path fill="#fff" d="M6.6 10.8a15.1 15.1 0 0 0 6.6 6.6l2.2-2.2c.3-.3.7-.4 1-.2 1.1.4 2.3.6 3.6.6.6 0 1 .4 1 1V20c0 .6-.4 1-1 1C10.6 21 3 13.4 3 4c0-.6.4-1 1-1h3.5c.6 0 1 .4 1 1 0 1.3.2 2.5.6 3.6.1.3 0 .7-.2 1z"/></svg>
        <span>555.204.7781</span>
      </div>
      <div class="footer-divider divider-two"></div>
      <div class="contact-item contact-address">
        <svg width="11" height="15" viewBox="0 0 12 16"><path fill="#fff" d="M6 0a6 6 0 0 0-6 6c0 4.5 6 10 6 10s6-5.5 6-10a6 6 0 0 0-6-6zm0 8.5A2.5 2.5 0 1 1 6 3.5a2.5 2.5 0 0 1 0 5z"/></svg>
        <span>480 Meridian Avenue<br>Lakeview, OH 43000</span>
      </div>
    </div>
  </div>
</body>
</html>
```